NEW Wordpress Website Design for a Dynamic Long Term Healthcare Company in Hawaii

I would like a new website design for my current company, Marlow Haven Partners, which has two different brands - Marlow Homecare and Marlow Senior Living. You can see the current website at www.marlowhaven.example. The website should be built using Wordpress Software and the Elementor theme. The website should have a local Hawaii island/tropical feel, but look professional for healthcare. I'm looking for something fresh, and want the designer to select colors, styles, etc.

In the Header, on all pages, I would like a menu that includes Home Care, Senior Living, Rates, and About Us.
Under each of the Header Menu Titles, I would like these drop downs included:
Home Care (drop down pages)- Nurse Aide Care, 24-Hour Home Care, Skilled Nursing, Lifestyle Aide, Hospice at Home, Bathing & Meal Service.
Senior Living (drop down pages) - Long-Term Stay, Short-Term Stay.
Rates (drop down page) - Rates.
About Us (drop down pages) - Our Mission, Ohana Talk, About Doreen Marlow.

In the footer, on all pages, you should include the address: 248 Lanakila Ave, Suite 310, Honolulu, HI 96817. Phone number: 808-555-0173
The footer should also include buttons for a page called Learn, Caregiver Jobs, and each of the service page links to include: Nurse Aide Care, 24-Hour Home Care, Skilled Nursing, Lifestyle Aide, Hospice at Home, Bathing & Meal Service.
Please don't take the current website and redesign a few aspects. I'm looking for a completely different look and feel.

Target Market(s)

40-80 year olds

Industry/Entity Type

Long Term Healthcare

Coding

Coded - Design and coding required

Requirements
Should not have
• Our existing website as a template. We are looking for a complete redesign. Thank you.

```html
<!DOCTYPE html>
<html lang="en">
<head>
<meta charset="utf-8">
<title>Marlow Haven Partners – Homecare &amp; Senior Living</title>
<link href="https://fonts.googleapis.com/css2?family=Playfair+Display:wght@600;700&family=Poppins:wght@400;500;600;700&display=swap" rel="stylesheet">
<style>
:root{
  --navy:#1b3668;
  --navy-deep:#142a52;
  --blue:#1689e0;
  --blue-soft:#5fb2ea;
  --ink:#24324a;
  --muted:#6b7588;
  --line:#dfe5ee;
  --pale:#f3f7fc;
  --white:#ffffff;
}
*{box-sizing:border-box;margin:0;padding:0}
html,body{width:1200px;height:3944px;overflow:hidden}
body{font-family:"Poppins",sans-serif;color:var(--ink);background:var(--white);position:relative;font-size:14px;line-height:1.6}
.serif{font-family:"Playfair Display",serif}
a{color:inherit;text-decoration:none}
.abs{position:absolute}

/* top bar */
.topbar{top:0;left:0;width:1200px;height:24px;background:var(--navy-deep);color:#fff;font-size:12px;text-align:center;line-height:24px;font-weight:500}

/* header */
.header{top:24px;left:0;width:1200px;height:96px;background:#fff;display:flex;align-items:center;padding-left:112px}
.brand{display:flex;align-items:center;gap:8px;font-weight:700;color:var(--navy);font-size:15px;line-height:1.1}
.brand .mark{width:16px;height:16px;border-radius:50%;background:var(--blue);flex:none}
.header .brand + .brand{margin-left:26px}
.header .call{position:absolute;left:640px;top:18px;font-size:11px;color:var(--navy);font-weight:600;display:flex;gap:6px;align-items:center}
.nav{position:absolute;left:640px;top:52px;display:flex;gap:22px;font-size:12px;font-weight:600;color:var(--navy);white-space:nowrap}
.nav .on{color:var(--blue);border-bottom:2px solid var(--blue);padding-bottom:4px}
.contact-btn{position:absolute;right:0;top:0;width:152px;height:96px;background:var(--blue);color:#fff;font-weight:700;font-size:14px;display:flex;align-items:center;justify-content:center}

/* hero */
.hero{top:120px;left:0;width:1200px;height:720px;background:linear-gradient(100deg,#1f4f6e 0%,#3f7f86 40%,#a8c4b4 70%,#d9d4c4 100%)}
.hero-copy{top:175px;left:112px;width:420px;color:#fff}
.hero-copy h1{font-size:52px;line-height:1.08;font-weight:700;margin-bottom:26px}
.hero-copy p{font-size:13px;line-height:1.65;margin-bottom:12px}
.btn{display:inline-block;background:var(--blue);color:#fff;font-size:12px;font-weight:600;padding:10px 18px;border-radius:3px;text-transform:uppercase}
.btn.light{background:#fff;color:var(--navy)}
.hero-tile{top:632px;height:208px;width:484px;color:#fff;font-size:26px;display:flex;align-items:center;justify-content:center}
.tile-home{left:112px;background:rgba(95,178,234,.85)}
.tile-senior{left:600px;background:rgba(27,54,104,.85)}

/* about */
.about-photo{top:912px;left:112px;width:300px;height:448px;background:linear-gradient(160deg,#c8d6e4,#8fa9c4);border-radius:6px}
.label{font-size:11px;font-weight:600;letter-spacing:1px;color:var(--blue);text-transform:uppercase}
.about-text{top:930px;left:640px;width:520px}
.about-text h2{font-size:32px;line-height:1.2;color:var(--navy);margin:8px 0 20px}
.about-text p{font-size:13px;color:var(--muted);margin-bottom:14px}

/* care band */
.band{top:1432px;height:408px;width:600px;color:#fff;text-align:center;padding:72px 70px 0}
.band-left{left:0;background:var(--navy)}
.band-right{left:600px;background:var(--blue)}
.band h3{font-size:26px;margin-bottom:14px}
.band p{font-size:14px;line-height:1.7;margin-bottom:28px}

/* services */
.services{top:1860px;left:0;width:1200px;height:620px;background:linear-gradient(90deg,#fff 55%,#e7eef0 80%,#d3dfe0 100%)}
.services-head{top:1894px;left:112px}
.services-head h2{font-size:34px;color:var(--navy);margin-top:6px}
.card{top:2000px;width:304px;height:408px;background:#fff;box-shadow:0 6px 20px rgba(20,42,82,.12)}
.card .pic{height:220px}
.card .body{padding:22px 20px}
.card h4{font-size:18px;color:var(--navy);margin-bottom:8px}
.card p{font-size:12px;color:var(--muted);line-height:1.55;margin-bottom:10px}
.more{font-size:11px;font-weight:700;color:var(--navy);display:flex;align-items:center;gap:6px}
.dots{display:flex;gap:8px}
.dots i{width:9px;height:9px;border-radius:50%;background:#c6ceda;display:block}
.dots i.on{background:var(--blue)}

/* reviews */
.reviews-head{top:2556px;left:0;width:1200px;text-align:center}
.reviews-head h2{font-size:34px;color:var(--navy);margin-top:6px}
.review-photo{top:2680px;width:160px;height:160px;border-radius:50%;background:linear-gradient(160deg,#e1e5ea,#aab4c2)}
.review{top:2690px;width:300px}
.review h5{font-size:17px;color:var(--navy);margin-bottom:8px;font-weight:600}
.review p{font-size:12px;color:var(--muted);margin-bottom:8px}
.review .who{font-size:12px;color:var(--ink);font-weight:500}
.quote{top:2670px;width:34px;height:34px;border-radius:50%;background:var(--blue);color:#fff;font-family:"Playfair Display",serif;font-size:26px;text-align:center;line-height:42px}

/* contact */
.contact-bg{top:2980px;left:0;width:1200px;height:640px;background:var(--pale)}
.contact-photo{top:3040px;left:0;width:560px;height:580px;background:linear-gradient(150deg,#e6dccf,#b9a591)}
.form-card{top:2940px;left:432px;width:616px;height:660px;background:#fff;box-shadow:0 10px 30px rgba(20,42,82,.15);padding:44px 60px}
.form-card h2{font-size:32px;color:var(--navy);margin:4px 0 22px}
.field{border-bottom:1px solid var(--line);font-size:12px;color:var(--muted);padding:10px 0 8px;margin-bottom:12px}
.note{font-size:11px;color:var(--muted);margin:6px 0 20px}
.note b{color:var(--ink);display:block}

/* footer */
.footer{top:3620px;left:0;width:1200px;height:268px;background:var(--navy);color:#fff}
.f-brands{top:3690px;left:112px;display:flex;flex-direction:column;gap:18px}
.f-brands .brand{color:#fff}
.f-brands .brand .mark{background:#fff}
.f-col{top:3660px;color:#fff}
.f-col h6{font-size:15px;font-weight:700;letter-spacing:.5px;margin-bottom:12px;text-transform:uppercase}
.f-col li{list-style:none;font-size:12px;line-height:2;color:#dbe4f2}
.f-contact{display:flex;gap:10px;margin-bottom:12px;font-size:12px;line-height:1.5;color:#dbe4f2}
.f-contact svg{flex:none;margin-top:2px}
.f-contact b{display:block;color:#fff;font-size:13px}
.bottombar{top:3888px;left:0;width:1200px;height:56px;background:var(--navy-deep);color:#c9d4e6;font-size:12px;display:flex;align-items:center;justify-content:center}
.mini-btns{left:112px;top:3904px;display:flex;gap:8px}
.mini-btns a{font-size:10px;font-weight:600;padding:5px 10px;background:var(--blue);color:#fff;border-radius:2px}
.mini-btns a + a{background:transparent;border:1px solid #fff}
</style>
</head>
<body>

<div class="abs topbar">Marlow Homecare Top Rated Homecare Since 1998</div>

<header class="abs header">
  <div class="brand"><span class="mark"></span>Marlow<br>Homecare</div>
  <div class="brand"><span class="mark"></span>Marlow<br>Senior Living</div>
  <div class="call">
    <svg width="12" height="12" viewBox="0 0 24 24"><path fill="#1689e0" d="M6.6 10.8a15 15 0 006.6 6.6l2.2-2.2a1 1 0 011-.25 11.4 11.4 0 003.6.57 1 1 0 011 1V20a1 1 0 01-1 1A17 17 0 013 4a1 1 0 011-1h3.5a1 1 0 011 1c0 1.25.2 2.45.57 3.6a1 1 0 01-.25 1z"/></svg>
    CALL US TODAY &nbsp;(808) 555-0173
  </div>
  <nav class="nav">
    <a class="on">HOME CARE ▾</a><a>ABOUT US ▾</a><a>SENIOR LIVING ▾</a><a>RATES ▾</a>
  </nav>
  <a class="contact-btn">CONTACT US</a>
</header>

<section class="abs hero" role="img" aria-label="Photo of a caregiver walking with a senior man using a walker on a tropical garden path"></section>
<div class="abs hero-copy">
  <h1 class="serif">Hawaii's Choice Homecare &amp; Senior Living</h1>
  <p>Marlow Homecare provides a variety of professional in-home health care services throughout the entire island of Oahu.</p>
  <p>Marlow Senior Living, a beautiful Adult Residential Care Home, is located on the windward side of Oahu in Kailua.</p>
  <a class="btn" style="margin-top:40px">Get Started</a>
</div>
<div class="abs hero-tile tile-home serif">Home Care</div>
<div class="abs hero-tile tile-senior serif">Senior Living</div>

<div class="abs about-photo" role="img" aria-label="Portrait of a smiling nurse with a stethoscope"></div>
<section class="abs about-text">
  <div class="label">About Us</div>
  <h2 class="serif">Welcome To Marlow Home Care &amp; Senior Living</h2>
  <p>At Marlow Haven Partners, our mission is to provide compassionate and professional long-term healthcare services that empower individuals to maintain their highest level of independence, health, and well-being in the comfort of their own homes or ours, either through our licensed home healthcare agency - Marlow Homecare, or in our Adult Residential Care Home - Marlow Senior Living.</p>
  <p>We are dedicated to delivering personalized care that addresses the unique needs of each client, fostering a sense of trust, respect, and dignity.</p>
  <a class="btn" style="margin-top:8px">Read More</a>
</section>

<section class="abs band band-left">
  <h3 class="serif">Professional Care In Your Home</h3>
  <p>Marlow Homecare understands that every person's care journey is unique. We tailor our in-home services to meet the diverse nurturing experience of professional quality care and safety within the comfort and convenience of your own home.</p>
  <a class="btn light">Schedule Care Assessment</a>
</section>
<section class="abs band band-right">
  <h3 class="serif">Trusted Care In Our Home</h3>
  <p>Marlow Senior Living creates a warm, supportive, and enriching care home environment where seniors can thrive in their golden years. We provide residential care that promotes well-being, connection, and dignity of each individual.</p>
  <a class="btn light">Schedule Tour</a>
</section>

<section class="abs services" role="img" aria-label="Soft background photo of a palm-lined tropical beach"></section>
<div class="abs services-head">
  <div class="label">What We Do</div>
  <h2 class="serif">Providing Quality Home Care &amp; Senior Living</h2>
</div>

<article class="abs card" style="left:112px">
  <div class="pic" role="img" aria-label="Photo of a caregiver helping a senior woman at home" style="background:linear-gradient(160deg,#d8dde3,#9fb0c0)"></div>
  <div class="body">
    <h4 class="serif">Lifestyle Aide</h4>
    <p>Lifestyle aid services focus on enhancing the overall quality of life for individuals. This can include assistance with daily routines.</p>
    <a class="more">MORE INFO <svg width="14" height="14" viewBox="0 0 24 24"><circle cx="12" cy="12" r="11" fill="#1b3668"/><path d="M10 7l5 5-5 5" stroke="#fff" stroke-width="2" fill="none"/></svg></a>
  </div>
</article>
<article class="abs card" style="left:448px">
  <div class="pic" role="img" aria-label="Photo of a nurse aide sharing a meal with a senior couple" style="background:linear-gradient(160deg,#e0d6c6,#b79e80)"></div>
  <div class="body">
    <h4 class="serif">Nurse Aide Care</h4>
    <p>Nurse aide care, also known as personal care or non-medical care, involves providing individuals with help in their daily tasks.</p>
    <a class="more">MORE INFO <svg width="14" height="14" viewBox="0 0 24 24"><circle cx="12" cy="12" r="11" fill="#1b3668"/><path d="M10 7l5 5-5 5" stroke="#fff" stroke-width="2" fill="none"/></svg></a>
  </div>
</article>
<article class="abs card" style="left:784px">
  <div class="pic" role="img" aria-label="Photo of a skilled nurse checking a senior patient" style="background:linear-gradient(160deg,#d6e3ef,#8aa8c6)"></div>
  <div class="body">
    <h4 class="serif">Skilled Nursing</h4>
    <p>Skilled nursing services are provided by licensed nurses, either Registered Nurses (RNs) or Licensed Practical Nurses.</p>
    <a class="more">MORE INFO <svg width="14" height="14" viewBox="0 0 24 24"><circle cx="12" cy="12" r="11" fill="#1b3668"/><path d="M10 7l5 5-5 5" stroke="#fff" stroke-width="2" fill="none"/></svg></a>
  </div>
</article>
<div class="abs dots" style="top:2436px;left:574px"><i class="on"></i><i></i><i></i></div>

<div class="abs reviews-head">
  <div class="label">Client Testimonials</div>
  <h2 class="serif">Client Reviews About Us</h2>
</div>
<div class="abs review-photo" style="left:112px" role="img" aria-label="Portrait of an elderly man client"></div>
<div class="abs quote" style="left:108px">“</div>
<div class="abs review" style="left:292px">
  <h5>Excellent Service</h5>
  <p>Kind staff cared for my father with patience and warmth every single day. They kept us informed, arrived on time and treated him like family. We are truly grateful for their help.</p>
  <div class="who">-Keoni Alvarez</div>
</div>
<div class="abs review-photo" style="left:640px" role="img" aria-label="Portrait of a smiling senior man client"></div>
<div class="abs quote" style="left:636px">“</div>
<div class="abs review" style="left:820px">
  <h5>Good Home Care</h5>
  <p>The caregivers made my mother feel safe and happy in her own home. Scheduling was easy, the nurses were skilled, and the whole team listened to our needs with real care.</p>
  <div class="who">-Malia Perreira</div>
</div>
<div class="abs dots" style="top:2880px;left:574px"><i></i><i class="on"></i><i></i></div>

<div class="abs contact-bg"></div>
<div class="abs contact-photo" role="img" aria-label="Photo of a caregiver embracing a smiling senior woman"></div>
<form class="abs form-card">
  <div class="label">Contact Us</div>
  <h2 class="serif">Touch With Us</h2>
  <div class="field">Name</div>
  <div class="field">Phone Number</div>
  <div class="field">Email</div>
  <div class="field">How Can We Help</div>
  <div class="field">Questions/Comments</div>
  <div class="field">May We Email You About This?</div>
  <div class="note"><b>Field is Required</b>You agree to receive future emails and understand you may opt-out at any time</div>
  <a class="btn">Submit</a>
</form>

<footer class="abs footer"></footer>
<div class="abs f-brands">
  <div class="brand"><span class="mark"></span>Marlow<br>Homecare</div>
  <div class="brand"><span class="mark"></span>Marlow<br>Senior Living</div>
</div>
<div class="abs f-col" style="left:452px">
  <h6>Quick Links</h6>
  <ul><li>Home Care</li><li>About Us</li><li>Senior Living</li><li>Rates</li></ul>
</div>
<div class="abs f-col" style="left:640px;width:260px">
  <h6>Contact Us</h6>
  <div class="f-contact"><svg width="16" height="16" viewBox="0 0 24 24"><path fill="#5fb2ea" d="M6.6 10.8a15 15 0 006.6 6.6l2.2-2.2a1 1 0 011-.25 11.4 11.4 0 003.6.57 1 1 0 011 1V20a1 1 0 01-1 1A17 17 0 013 4a1 1 0 011-1h3.5a1 1 0 011 1c0 1.25.2 2.45.57 3.6a1 1 0 01-.25 1z"/></svg><div><b>Phone No:</b>(808) 555-0173</div></div>
  <div class="f-contact"><svg width="16" height="16" viewBox="0 0 24 24"><rect x="2" y="5" width="20" height="14" rx="2" fill="#5fb2ea"/><path d="M3 6l9 7 9-7" stroke="#1b3668" stroke-width="1.6" fill="none"/></svg><div><b>Email:</b>info@marlowhaven.example</div></div>
  <div class="f-contact"><svg width="16" height="16" viewBox="0 0 24 24"><path fill="#5fb2ea" d="M12 2a7 7 0 017 7c0 5-7 13-7 13S5 14 5 9a7 7 0 017-7zm0 4.5A2.5 2.5 0 1012 11.5 2.5 2.5 0 0012 6.5z"/></svg><div><b>Location:</b>248 Lanakila Ave, Suite 310<br>Honolulu, HI 96817</div></div>
</div>
<div class="abs f-col" style="left:920px">
  <h6>Service Links</h6>
  <ul><li>Nurse Aide Care</li><li>24-Hour Home Care</li><li>Skilled Nursing</li><li>Lifestyle Aide</li><li>Hospice at Home</li><li>Bathing &amp; Meal Service</li></ul>
</div>
<div class="abs bottombar">© 2024 Marlow Haven Partners. All Rights Reserved.</div>
<div class="abs mini-btns"><a>LEARN</a><a>CAREGIVER JOBS</a></div>

</body>
</html>
```